Brambleton Resource Holdings, LP Letter Head

We need an official company letter head design that is clean and mimics our company logo style. It will include our logo, address, phone, and website. We are an OIl and Gas mineral purchasing company, so hints of oil rigs or related design would be desirable.

Industry/Entity Type

Oil And Gas

Colors
ec1f27
f04a50
f59195
fbd4d5

Requirements
Must have
• Logo
• 7392 Whitcombe R. Ashdale Parkway, Suite 618
• Dallas TX, 75391
• 214-673-1958
• www.bramblestoneres.example
Nice to have
• Oil Rigs or OIl and gas related design

```html
<!DOCTYPE html>
<html lang="en">
<head>
<meta charset="utf-8">
<title>Brambleton Resource Holdings, LP Letterhead</title>
<link rel="stylesheet" href="https://fonts.googleapis.com/css2?family=Open+Sans:wght@400;600&family=PT+Sans:wght@400;700&family=Great+Vibes&display=swap">
<style>
  :root {
    --brand-red: #ec1f27;
    --brand-red-soft: #f59195;
    --ink: #1c1c1c;
    --body-ink: #4a4a4a;
    --wave-grey: #58595b;
    --paper: #ffffff;
    --backdrop: #e6e6e6;
  }
  * { margin: 0; padding: 0; box-sizing: border-box; }
  html, body {
    width: 985px; height: 1200px; overflow: hidden;
    background: var(--backdrop);
  }
  .letterhead {
    position: absolute; left: 52px; top: 26px;
    width: 880px; height: 1148px;
    background: var(--paper);
    overflow: hidden;
    font-family: "PT Sans", sans-serif;
  }
  .brand {
    position: absolute; left: 70px; top: 56px;
    display: flex; flex-direction: column; align-items: center;
    width: 220px;
  }
  .brand-square {
    width: 85px; height: 85px;
    background: var(--brand-red);
  }
  .brand-name {
    margin-top: 14px;
    font-family: "PT Sans", sans-serif;
    font-weight: 400; font-size: 25px; line-height: 1.05;
    color: var(--brand-red); text-align: center;
  }
  .sender-address {
    position: absolute; right: 67px; top: 103px;
    font-family: "Open Sans", sans-serif; font-weight: 600;
    font-size: 11.5px; line-height: 17px;
    color: #333; text-align: right;
  }
  .letter-title {
    position: absolute; left: 73px; top: 268px;
    font-size: 20px; font-weight: 700; color: var(--ink);
  }
  .letter-body {
    position: absolute; left: 73px; top: 314px; width: 751px;
    font-size: 14.2px; line-height: 19.1px;
    color: var(--body-ink); text-align: justify; hyphens: auto;
  }
  .letter-body p + p { margin-top: 19px; }
  .signature {
    position: absolute; right: 54px; top: 904px;
    font-family: "Great Vibes", cursive; font-size: 34px;
    color: #777;
  }
  .footer-wave {
    position: absolute; left: 0; bottom: 0; width: 880px; height: 271px;
  }
  .rig-mark {
    position: absolute; left: 34px; top: 1036px;
    width: 62px; height: 79px;
    background: var(--brand-red-soft); opacity: .85;
  }
  .footer-web {
    position: absolute; right: 50px; top: 1084px;
    font-family: "Open Sans", sans-serif; font-weight: 600;
    font-size: 13px; letter-spacing: 1px; color: #fff;
  }
</style>
</head>
<body>
  <main class="letterhead">
    <header>
      <div class="brand">
        <div class="brand-square"></div>
        <div class="brand-name">Brambleton Resource Holdings</div>
      </div>
      <address class="sender-address" style="font-style:normal">
        7392 Whitcombe R. Ashdale Parkway, Suite<br>
        618, Dallas TX, 75391, P:214-673-1958
      </address>
    </header>

    <h1 class="letter-title">Lorem ipsum dolor sit amet</h1>

    <section class="letter-body">
      <p>Lorem ipsum dolor sit amet, consectetur adipiscing elit, sed do eiusmod tempor incididunt ut labore et dolore magna aliqua. Ut enim ad minim veniam, quis nostrud exercitation ullamco laboris nisi ut aliquip ex ea commodo consequat. Duis aute irure dolor in reprehenderit in voluptate velit esse cillum dolore eu fugiat nulla pariatur. Excepteur sint occaecat cupidatat non proident, sunt in culpa qui officia deserunt mollit anim id est laborum Sed ut perspiciatis unde omnis iste natus error sit voluptatem accusantium doloremque laudantium, totam rem aperiam, eaque ipsa quae ab illo inventore veritatis et quasi architecto beatae vitae dicta sunt explicabo. Nemo enim ipsam voluptatem quia voluptas sit aspernatur aut odit aut fugit, sed quia consequuntur magni dolores eos qui ratione voluptatem sequi nesciunt. Neque porro quisquam est, qui dolorem ipsum quia dolor sit amet, consectetur, adipisci velit, sed quia non numquam eius modi tempora incidunt ut labore et dolore magnam aliquam quaerat voluptatem. Ut enim ad minima veniam, quis nostrum exercitationem ullam corporis suscipit laboriosam, nisi ut aliquid ex ea commodi consequatur? Quis autem vel eum iure reprehenderit qui in ea voluptate velit esse quam nihil molestiae consequatur, vel illum qui dolorem eum fugiat quo voluptas nulla pariatur?</p>
      <p>Lorem ipsum dolor sit amet, consectetur adipiscing elit, sed do eiusmod tempor incididunt ut labore et dolore magna aliqua. Ut enim ad minim veniam, quis nostrud exercitation ullamco laboris nisi ut aliquip ex ea commodo consequat. Duis aute irure dolor in reprehenderit in voluptate velit esse cillum dolore eu fugiat nulla pariatur. Excepteur sint occaecat cupidatat non proident, sunt in culpa qui officia deserunt mollit anim id est laborum Sed ut perspiciatis unde omnis iste natus error sit voluptatem accusantium doloremque laudantium, totam rem aperiam, eaque ipsa quae ab illo inventore veritatis et quasi architecto beatae vitae dicta sunt explicabo. Nemo enim ipsam voluptatem quia voluptas sit aspernatur aut odit aut fugit, sed quia consequuntur magni dolores eos qui ratione voluptatem sequi nesciunt. Neque porro quisquam est, qui dolorem ipsum quia dolor sit amet, consectetur, adipisci velit, sed quia non numquam eius modi tempora incidunt ut labore et dolore magnam aliquam quaerat voluptatem. Ut enim ad minima veniam, quis nostrum exercitationem ullam corporis suscipit laboriosam, nisi ut aliquid ex ea commodi consequatur? Quis autem vel eum iure reprehenderit qui in ea voluptate velit esse quam nihil molestiae consequatur, vel illum qui dolorem eum fugiat quo voluptas nulla pariatur?</p>
      <p>Lorem ipsum dolor sit amet, consectetur adipiscing elit, sed do eiusmod tempor incididunt ut labore et dolore magna aliqua. Ut enim ad minim veniam, quis nostrud exercitation ullamco laboris nisi ut aliquip ex ea commodo consequat. Duis aute irure dolor in reprehenderit in voluptate velit esse cillum dolore eu fugiat nulla pariatur.</p>
    </section>

    <div class="signature">Signature</div>

    <svg class="footer-wave" viewBox="0 778 780 240" preserveAspectRatio="none" aria-hidden="true">
      <path d="M0,808 C120,905 260,935 420,928 C560,921 680,913 780,918 L780,1018 L0,1018 Z" fill="var(--brand-red)"/>
      <path d="M-2,782 C120,884 260,916 420,909 C560,902 680,894 782,902" fill="none" stroke="var(--wave-grey)" stroke-width="11"/>
    </svg>

    <div class="rig-mark" role="img" aria-label="Small offshore oil rig emblem"></div>
    <div class="footer-web">www.bramblestoneres.example</div>
  </main>
</body>
</html>
```